Scientific Poster- Immunology Marcus T

I have all the information, but need this placed in a design format where it can be printed. The size will need to be 1meter by 1 meter. I just have the basic text and images. I just need the design around that added to make it look more attractive.
Please see some of the examples online, with web link below.

Target Market(s)

Scientific Meeting

Font styles to use
Sans Serif

Requirements
Must have
• Professional appearance
Nice to have
• examples can be found on
• https://www.orvelmintprints.com/sample_gallery_pages
Should not have
• Should be professional

```html
<!DOCTYPE html>
<html lang="en">
<head>
<meta charset="utf-8">
<title>Image Guided Cryoablation – Scientific Poster</title>
<link href="https://fonts.googleapis.com/css2?family=Marcellus+SC&family=Open+Sans:wght@400;600;700&display=swap" rel="stylesheet">
<style>
:root{
  --navy:#1c5a7e;
  --gold:#f5c518;
  --bar-gold:#fcc419;
  --paper:#d3d4d6;
  --abstract:#fdf4a6;
  --ink:#2a2a2a;
  --teal:#4f9b8c;
  --scan-dark:#1a1d22;
  --scan-pet:#23307a;
}
*{margin:0;padding:0;box-sizing:border-box}
html,body{width:1200px;height:1200px;overflow:hidden}
body{position:relative;background:var(--paper);font-family:"Open Sans",Arial,sans-serif;color:var(--ink)}
.backdrop{position:absolute;inset:0}
.title{position:absolute;left:0;top:88px;width:1200px;text-align:center;font-family:"Marcellus SC",Georgia,serif;color:var(--gold);font-size:41px;line-height:51px;letter-spacing:-.3px}
.title-rule{position:absolute;left:84px;top:249px;width:1032px;height:2px;background:#fff}
.authors{position:absolute;left:0;top:262px;width:1200px;text-align:center;color:#fff;font-weight:700;font-size:22px}
.authors span{margin:0 10px}
.abstract{position:absolute;left:56px;top:330px;width:1088px;height:400px;background:var(--abstract);border:1.5px solid #222;border-radius:24px}
.abstract-title{position:absolute;top:24px;width:100%;text-align:center;font-weight:700;font-size:15px;letter-spacing:11px}
.abs-col{position:absolute;top:58px}
.abs-col h2{background:var(--bar-gold);font-size:15px;font-weight:700;padding:1px 15px;height:20px;line-height:18px;margin-bottom:8px}
.abs-col p{font-size:12.4px;line-height:15.2px}
.abs-div{position:absolute;top:60px;width:1px;height:310px;background:#777}
.patient{position:absolute;top:748px}
.patient h3{background:var(--navy);color:var(--gold);font-size:10px;font-weight:700;padding:0 12px;height:15px;line-height:15px}
.patient .story{font-size:9.4px;line-height:11.4px;margin-top:4px}
.col-div{position:absolute;top:768px;width:1.5px;height:390px;background:var(--teal)}
.scan{position:absolute;background:var(--scan-dark);border:1px solid #555}
.scan.pet{background:radial-gradient(ellipse at center,#4a5cc0 0%,var(--scan-pet) 55%,#0d1238 100%)}
.scan.ct{background:radial-gradient(ellipse at center,#8d8f93 0%,#3a3d42 50%,#0e0f12 100%)}
.scan.lung{background:radial-gradient(ellipse at center,#cfd1d4 0%,#6a6c70 60%,#101114 100%)}
.cap{position:absolute;font-size:7.6px;line-height:9.2px;color:#333}
.footer-line{position:absolute;top:1171px;height:2px;background:var(--teal)}
.email{position:absolute;top:1162px;left:0;width:1200px;text-align:center;color:var(--navy);font-weight:700;font-size:14px;letter-spacing:2px}
</style>
</head>
<body>
<svg class="backdrop" width="1200" height="1200" aria-hidden="true">
  <polygon points="0,0 1200,0 1200,352 0,430" fill="#1c5a7e"/>
</svg>

<h1 class="title">Image Guided Cryoablation of<br>cancer with intra-tumor Injection of anti-CTLA-4<br>and PD-1 immune checkpoint inhibitors</h1>
<div class="title-rule"></div>
<p class="authors">Marcus R. Talbot MD <span>|</span> Daniel E. Harrow MD <span>|</span> Leon A. Fairburn MD</p>

<section class="abstract">
  <div class="abstract-title">ABSTRACT:</div>
  <div class="abs-col" style="left:28px;width:148px">
    <h2>HYPOTHESIS:</h2>
    <p>In situ Image Guided Cancer Cryoablation combined with image guided injection of immune check-point inhibitors is an effective method of treating local and systemic malignancy. The inflammatory cytokines and release of tumor antigens from Cryoablation, combined with immune check-point inhibitors can create an in-situ tumor vaccine resulting in a systemic anti-cancer immune response.</p>
  </div>
  <div class="abs-div" style="left:194px"></div>
  <div class="abs-col" style="left:208px;width:322px">
    <h2>METHODS:</h2>
    <p>Patients participating in an ongoing research protocol underwent in situ Image Guided Cryoablation of one or more malignant cancers. Image guidance included Computed Tomography and/or Ultrasound. The Cryoablation procedure was performed using standard well developed and described percutaneous techniques. For the procedure, each patient received either IV or general anesthesia. Immediately following the cryoablation of cancer, each cryo-treated tumor was injected with a combination of Ipilimumab/Nivolumab or Ipilimumab/Pembrolizumab immune checkpoint inhibitors. The injection was performed with 50% of the systemic dose of 3mg/kg. The patients remained monitored inpatients for 24-48 hours post surgery. Follow-up with serum tumor markers where applicable, CBC, and serum chemistries were obtained at 1 week and every month post procedure. Cross sectional Imaging was obtained at 3-4 weeks and at every 3 months post procedure.</p>
  </div>
  <div class="abs-div" style="left:545px"></div>
  <div class="abs-col" style="left:562px;width:222px">
    <h2>RESULTS:</h2>
    <p>Patients treated with in situ tumor cryoablation demonstrated the expected macro cellular cryo-necrosis with morphologic changes in the treated tissue, which was evident as early as 6 hours postop. With more time, the treated tumor morphology was noted to deviate from the standard cryoablation decay with some patients having rapid large volume tissue decay far exceeding that expected from cryoablation alone. In the non treated tumor as identified on cross sectional imaging, distant tumor deposits were noted to decrease in size and many to disappear. At 6 months post treatment there has been no recurrence of responding tumor.</p>
  </div>
  <div class="abs-div" style="left:799px"></div>
  <div class="abs-col" style="left:814px;width:246px">
    <h2>CONCLUSION:</h2>
    <p>The combination of intra-tumoral checkpoint inhibitor injection with percutaneous cryoablation of metastatic malignancy shows great promise in providing a far superior treatment methodology than either method alone, has previously shown. It has been known that ablation techniques, especially Cryoablation can generate an anti-tumor immune response; however, this is rarely curative. These cases show that the combination of immune checkpoint inhibitors with Cryoablation generates a synergy, effectively creating a tumor vaccine, which can cause the resolution of not only the local treated area, but also a systemic response eradicating all visible disease. Further data from this study will better refine this conclusion.</p>
  </div>
</section>

<section class="patient" style="left:56px;width:286px">
  <h3>PATIENT #1</h3>
  <p class="story">Patient is a 58-year-old female with a seven-year history of tumor of unknown origin, presumed breast. She had prior standard of care treatment with chemotherapy and radiation. The patient had failed all standard options and continued to have progression with numerous tumors in the lungs and thoracic lymph nodes. The patient was then treated with image-guided ablation combined with Ipilimumab and Pembrolizumab.</p>
</section>
<div class="scan pet" style="left:56px;top:860px;width:78px;height:44px" role="img" aria-label="FDG PET/CT axial chest scan"></div>
<p class="cap" style="left:143px;top:868px;width:196px">Image above demonstrates FDG PET/CT with abnormal uptake in bilateral infra- hilar and right peri-aortic lymph nodes.</p>
<div class="scan pet" style="left:56px;top:916px;width:78px;height:44px" role="img" aria-label="FDG PET/CT axial chest scan"></div>
<p class="cap" style="left:143px;top:919px;width:196px">Image above demonstrates FDG PET/CT with abnormal uptake in right supra-hilar lymph nodes, right upper lobe nodule and right axillary lymph node.</p>
<div class="scan ct" style="left:56px;top:974px;width:78px;height:50px" role="img" aria-label="CT scan with ablation needle in right upper lobe"></div>
<p class="cap" style="left:143px;top:984px;width:196px">Image above is a CT scan performed during the ablation procedure demonstrating ablation needle with a right upper lobe lesion.</p>
<div class="scan pet" style="left:56px;top:1035px;width:78px;height:44px" role="img" aria-label="Follow-up FDG PET/CT scan at 2 months"></div>
<p class="cap" style="left:143px;top:1043px;width:196px">The image above demonstrates a FDG PET/CT scan performed 2 months after treatment with minimal peripheral FDG uptake of the ablated tumor site.</p>
<div class="scan pet" style="left:56px;top:1089px;width:78px;height:44px" role="img" aria-label="Follow-up FDG PET/CT scan showing resolution"></div>
<p class="cap" style="left:143px;top:1093px;width:196px">The above image is a FDG PET/CT performed 2 months after treatment showing resolution of infra-hilar adenopathy, with minimal residual uptake in peri-aortic adenopathy.</p>

<div class="col-div" style="left:365px"></div>

<section class="patient" style="left:390px;width:356px">
  <h3>PATIENT #2</h3>
  <p class="story">Patient is a 68 year old male with a 2 year history of a left renal mass. The patient underwent a left nephrectomy with a diagnosis of renal cell carcinoma. A subsequent CT scan demonstrated numerous lung nodules (&gt;20) and a large L5 vertebral body mass. The patient was then treated with Cryoablation of the L5 mass with intra-tumoral injection of Ipilimumab and Nivolumab into the ablated tumor site. A follow up CT scan 7 weeks after treatment demonstrated complete resolution of the lung nodules with a stable L5 mass.</p>
</section>
<div class="scan lung" style="left:392px;top:862px;width:72px;height:72px" role="img" aria-label="Chest CT with lung nodule"></div>
<div class="scan lung" style="left:485px;top:862px;width:72px;height:72px" role="img" aria-label="Chest CT with bilateral lung nodules"></div>
<div class="scan lung" style="left:578px;top:862px;width:72px;height:72px" role="img" aria-label="Chest CT with additional lung nodule"></div>
<div class="scan ct" style="left:672px;top:862px;width:72px;height:72px" role="img" aria-label="CT of lumbar spine with L5 mass"></div>
<p class="cap" style="left:392px;top:943px;width:74px">The image above demonstrates a CT scan of the chest with a lung nodule.</p>
<p class="cap" style="left:485px;top:943px;width:76px">CT scan of the chest demonstrates multiple bilateral lung nodules.</p>
<p class="cap" style="left:578px;top:943px;width:76px">CT scan of the chest demonstrating additional lung nodule.</p>
<p class="cap" style="left:672px;top:943px;width:72px">CT scan of the lumbar spine demonstrating L5 mass.</p>
<div class="scan ct" style="left:392px;top:1006px;width:72px;height:72px" role="img" aria-label="CT during cryoablation of L5 mass"></div>
<div class="scan lung" style="left:485px;top:1006px;width:72px;height:72px" role="img" aria-label="Chest CT 7 weeks after procedure"></div>
<div class="scan lung" style="left:578px;top:1006px;width:72px;height:72px" role="img" aria-label="Chest CT 7 weeks after procedure"></div>
<div class="scan ct" style="left:672px;top:1006px;width:72px;height:72px" role="img" aria-label="Lumbar spine CT 7 weeks after treatment"></div>
<p class="cap" style="left:392px;top:1087px;width:74px">CT scan during ablation procedure demonstrating Cryoablation of L5 mass.</p>
<p class="cap" style="left:485px;top:1087px;width:76px">CT scan 7 weeks after procedure demonstrating resolution of lung nodules.</p>
<p class="cap" style="left:578px;top:1087px;width:76px">CT scan 7 weeks after procedure demonstrating resolution of lung nodules.</p>
<p class="cap" style="left:672px;top:1087px;width:72px">CT scan of the lumbar spine 7 weeks after treatment demonstrating stable lumbar mass</p>

<div class="col-div" style="left:766px"></div>

<section class="patient" style="left:793px;width:350px">
  <h3>PATIENT #3</h3>
  <p class="story">Patient is a 54 year old female with a several year history of breast cancer who then developed non-small cell lung cancer. The patient underwent several years of treatment with standard chemotherapy and radiation. The patient then developed a new large lung mass with mediastina adenopathy. A new biopsy was performed demonstrating malignancy of neuroendocrine type. The patient, opted for no further chemotherapy, but did agree to Cryoablation combined with intra-tumoral injection of Ipilimumab and Nivolumab. Due to the large volume of tumor, only a small area of tumor was ablated and treated. However, by 2 months, the patient demonstrated a whole body systemic response with resolution of tumors beyond the ablation site. This further supports that ablation combined with immune checkpoint inhibitors can create a systemic, anti-tumor immune response, essentially an in-situ tumor vaccine.</p>
</section>
<div class="scan pet" style="left:796px;top:914px;width:74px;height:73px" role="img" aria-label="PET/CT with right hilar and subcarinal uptake"></div>
<p class="cap" style="left:876px;top:915px;width:70px">Image demonstrates PET/CT with abnormal right hilar and subcarinal lymph nodes.</p>
<div class="scan ct" style="left:981px;top:914px;width:76px;height:73px" role="img" aria-label="Chest CT with large mediastinal and right hilar mass"></div>
<p class="cap" style="left:1063px;top:915px;width:80px">Image demonstrates a large mediastina and right hilar mass prior to the Cryoablation procedure combined with immune checkpoint injection.</p>
<div class="scan ct" style="left:796px;top:1005px;width:74px;height:75px" role="img" aria-label="CT with cryoablation needle in subcarinal node"></div>
<div class="scan ct" style="left:886px;top:1005px;width:74px;height:75px" role="img" aria-label="CT with low attenuation in treated subcarinal node"></div>
<div class="scan ct" style="left:976px;top:1005px;width:74px;height:75px" role="img" aria-label="One month follow-up chest CT"></div>
<div class="scan pet" style="left:1066px;top:1005px;width:74px;height:75px" role="img" aria-label="Two month follow-up PET/CT"></div>
<p class="cap" style="left:796px;top:1087px;width:80px">Image demonstrates Cryoablation procedure with the needle placed within the subcarinal lymph node.</p>
<p class="cap" style="left:886px;top:1087px;width:80px">Image demonstrates normal expected low attenuation with the treated subcarinal lymph node, which is a typical post Cryoablation appearance.</p>
<p class="cap" style="left:976px;top:1087px;width:80px">One month follow up CT demonstrates significant reduction in the associated mediastina and right hilar mass.</p>
<p class="cap" style="left:1066px;top:1087px;width:78px">Two month follow up PET/CT shows resolution of mediastina and right hilar masses.</p>

<div class="footer-line" style="left:56px;width:390px"></div>
<div class="footer-line" style="left:766px;width:378px"></div>
<p class="email">drtalbot@orvelmintbio.com</p>
</body>
</html>
```